Business card for Luxury Portable Restroom Trailer company

We are a Luxury Portable Restroom Trailer Company Called PELIKAR HIRES. Based in Orange County California. We provide portable restroom trailers for events, such as, Weddings, Concerts, Charity events, Sporting events, Tournaments, Corporate events, ect. We rent and Sell the Luxury restrooms. Our colors are white, grey, and Orange. As you will see in the logo we uploaded.
There are 2 people in the company so the names and titles will change for the 3 people but card will remain the same. Here is the information for each Person: Dennis Moyle CFO 555 018-3647
next Person: Wesley Tanford VP 555 018-3647
Next Person: Miles Tanford CEO 555 018-3647
Information to include on the card: Luxury Restroom Trailers Rental and Sales. Weddings, Concerts, Charity, Sporting and Corp. Events.

```html
<!DOCTYPE html>
<html lang="en">
<head>
<meta charset="utf-8">
<title>PELIKAR HIRES – Business Cards</title>
<link rel="stylesheet" href="https://fonts.googleapis.com/css2?family=Nunito:wght@700&family=Fira+Sans+Extra+Condensed:wght@500&display=swap">
<style>
  :root {
    --page-bg: #19191b;
    --card-grey: #5d5954;
    --card-white: #ffffff;
    --brand-orange: #f37021;
    --text-font: "Nunito", sans-serif;
    --name-font: "Fira Sans Extra Condensed", sans-serif;
  }
  * { margin: 0; padding: 0; box-sizing: border-box; }
  html, body {
    width: 1200px; height: 1200px; overflow: hidden;
    background: var(--page-bg);
  }
  .sheet { position: relative; width: 1200px; height: 1200px; }

  .card {
    position: absolute;
    background: var(--card-grey);
    overflow: hidden;
  }
  .card--front { left: 50px; top: 163px; width: 500px; height: 278px; }
  .card--dennis { left: 656px; top: 164px; width: 487px; height: 272px; }
  .card--wesley { left: 53px; top: 754px; width: 495px; height: 292px; }
  .card--miles { left: 658px; top: 757px; width: 483px; height: 285px; }

  /* front */
  .front-ring {
    position: absolute; left: 50%; top: 40%;
    width: 162px; height: 162px;
    transform: translate(-50%, -50%);
    border: 6px solid var(--brand-orange);
    border-radius: 50%;
  }
  .front-name {
    position: absolute; left: 0; right: 0; top: 72%;
    text-align: center;
    font-family: var(--text-font); font-weight: 700;
    font-size: 27px; letter-spacing: 1px;
    color: var(--brand-orange);
  }

  /* back */
  .diagonal { position: absolute; inset: 0; width: 100%; height: 100%; }
  .diagonal polygon { fill: var(--card-white); }
  .faint-ring {
    position: absolute; left: 50%; top: 40%;
    width: 156px; height: 156px;
    transform: translate(-50%, -50%);
    border: 5px solid var(--brand-orange);
    border-radius: 50%;
    opacity: 0.15;
  }
  .back-name {
    position: absolute; left: 6%; top: 13%;
    font-family: var(--text-font); font-weight: 700;
    font-size: 29px; letter-spacing: 1px;
    color: var(--brand-orange);
    white-space: nowrap;
  }
  .contact {
    position: absolute; right: 4.5%; top: 60%;
    font-family: var(--name-font); font-weight: 500;
    font-size: 27px; letter-spacing: -0.5px;
    color: var(--brand-orange);
    white-space: nowrap;
  }
  .tagline {
    position: absolute; right: 4.5%; top: 79%;
    text-align: right;
    font-family: var(--text-font); font-weight: 700;
    font-size: 11.5px; line-height: 16px;
    color: var(--brand-orange);
    white-space: nowrap;
  }
</style>
</head>
<body>
<main class="sheet">
  <section class="card card--front">
    <div class="front-ring"></div>
    <p class="front-name">PELIKAR HIRES</p>
  </section>

  <section class="card card--dennis">
    <svg class="diagonal" viewBox="0 0 100 100" preserveAspectRatio="none"><polygon points="100,0 100,100 0,100"/></svg>
    <div class="faint-ring"></div>
    <p class="back-name">PELIKAR HIRES</p>
    <p class="contact">Dennis Moyle CFO 555 018-3647</p>
    <p class="tagline">Luxury Restroom Trailers Rental and Sales.<br>Weddings, Concerts, Charity, Sporting and Corp. Events.</p>
  </section>

  <section class="card card--wesley">
    <svg class="diagonal" viewBox="0 0 100 100" preserveAspectRatio="none"><polygon points="100,0 100,100 0,100"/></svg>
    <div class="faint-ring"></div>
    <p class="back-name">PELIKAR HIRES</p>
    <p class="contact">Wesley Tanford VP 555 018-3647</p>
    <p class="tagline">Luxury Restroom Trailers Rental and Sales.<br>Weddings, Concerts, Charity, Sporting and Corp. Events.</p>
  </section>

  <section class="card card--miles">
    <svg class="diagonal" viewBox="0 0 100 100" preserveAspectRatio="none"><polygon points="100,0 100,100 0,100"/></svg>
    <div class="faint-ring"></div>
    <p class="back-name">PELIKAR HIRES</p>
    <p class="contact">Miles Tanford CEO 555 018-3647</p>
    <p class="tagline">Luxury Restroom Trailers Rental and Sales.<br>Weddings, Concerts, Charity, Sporting and Corp. Events.</p>
  </section>
</main>
</body>
</html>
```